Web Design Project

We are a business based in Sydney Australia, we have a very cool and sophisticated AI platform that lets you create Virtual Agents mainly for Enterprise clients but we are now moving into the Personal AI space where we will have mobile apps using our technology. We need a new look and feel with some better branding

We will progress this in stages with a quick touch up to our site followed by a more thorough rebuild.

So for now, on our web site, stage 1.... I'm happy to change colours, we will keep the "head" in our logo but change our name. if you look at out site at www.mylumenfold.example you will see that there is content but not much structure...we will include videos at some point and some infographics but not just yet ....so I'm after a suite of 3 different template designs that we can use and I want to work with the successful designer to tweak them and populate them with a lot of our current content.

We will keep our avatar but she may need a makeover...I'm open to suggestions on how to make our site more progressive. Would a more tiled, panelos 5 look and feel work?

I would prefer to use word press

Target Market(s)

mainly enterprise clients, big banks, insurance companies, telcos

Industry/Entity Type

Business

Requirements
Nice to have
• check out some of our competitors....brivoQA, TelmaRi, amber lattice, dorvaspark, quarnoreply, hOlpa

I was thinking that a more tiled 'panelos 5' look and feel might be good...open to suggestions
Should not have
• can't look cheap and nasty

```html
<!DOCTYPE html>
<html lang="en">
<head>
<meta charset="utf-8">
<title>My Lumenfold</title>
<link rel="stylesheet" href="https://fonts.googleapis.com/css2?family=Arimo:wght@400;700&family=Questrial&display=swap">
<style>
:root{
  --ink:#222;
  --text:#333;
  --teal:#2e8c7a;
  --teal-light:#4fb3a0;
  --teal-tile:#4aae99;
  --dark-btn:#3a3a3a;
  --hero-bg:#e6e7e8;
  --section-bg:#f1f1f1;
  --footer-bg:#2b2b2b;
  --footer-text:#c8c8c8;
  --plan-ent:#5c5c5c;
  --plan-pro:#333;
  --plan-per:#050505;
  --red:#c3000b;
  --brown:#3a2218;
}
*{margin:0;padding:0;box-sizing:border-box}
html,body{width:1200px;height:1148px;overflow:hidden;background:#fff}
body{font-family:"Arimo",Arial,sans-serif;color:var(--text)}
.page{position:relative;width:1150px;height:1100px;transform:scale(1.04348);transform-origin:0 0;background:#fff}
.abs{position:absolute}
.topline{left:0;top:0;width:1150px;height:6px;background:#333}
.header{left:0;top:6px;width:1150px;height:124px;background:linear-gradient(#f4f4f4,#fff)}
.brand{left:88px;top:38px;display:flex;align-items:center;gap:14px}
.brand-name{font-family:"Questrial",Arial,sans-serif;font-size:38px;letter-spacing:1px;color:var(--ink)}
.brand-mark{width:40px;height:40px;border-radius:50%;background:var(--teal)}
.account{left:904px;top:48px;display:flex;gap:4px}
.btn-dark{display:inline-block;background:linear-gradient(#555,#2c2c2c);color:#fff;font-weight:700;font-size:13px;height:28px;line-height:28px;padding:0 12px;border-radius:2px}
.hero{left:0;top:130px;width:1150px;height:402px;background:radial-gradient(ellipse at 30% 45%,#fafafa 0%,#ececed 45%,var(--hero-bg) 100%)}
.nav{left:86px;top:105px;width:978px;height:48px;background:linear-gradient(var(--teal-light),var(--teal));border-radius:2px;display:flex;box-shadow:0 6px 8px -4px rgba(0,0,0,.35)}
.nav a{color:#fff;text-decoration:none;font-weight:700;font-size:13px;line-height:48px;text-align:center;border-right:1px solid rgba(0,0,0,.15);box-shadow:1px 0 0 rgba(255,255,255,.2)}
.nav a.active{background:rgba(0,0,0,.08)}
.search{position:absolute;left:755px;top:10px;width:211px;height:27px;background:#fff;border:1px solid #bbb;font-size:11px;color:#888;line-height:25px;padding-left:12px}
.search svg{position:absolute;right:8px;top:5px}
.hero-title{left:114px;top:217px;font-size:22px;font-weight:700;color:var(--teal)}
.hero-copy{left:114px;top:253px;width:410px;font-size:13.4px;line-height:22px;text-align:justify;color:var(--text)}
.hero-more{left:114px;top:399px;height:31px;line-height:31px;font-size:13px}
.dots{left:116px;top:490px;display:flex;gap:10px}
.dots span{width:13px;height:13px;border-radius:50%;background:#999;box-shadow:inset 0 1px 2px rgba(0,0,0,.3)}
.dots span.on{background:#444}
.monitor{left:627px;top:196px;width:392px;height:270px;background:#2a2a2a;border-radius:10px 10px 8px 8px;overflow:hidden}
.screen{position:absolute;left:14px;top:14px;width:364px;height:208px;background:linear-gradient(#dfe6ee,#b9c7d4 60%,#e9edf1)}
.chin{position:absolute;left:0;bottom:0;width:392px;height:48px;background:linear-gradient(#d6d6d6,#aaa)}
.play{position:absolute;left:161px;top:78px;width:72px;height:50px;background:#111;border-radius:9px;border:1px solid #555}
.stand{left:760px;top:465px}
.sep{left:0;top:532px;width:1150px;height:8px;background:#fff}
.section{left:0;top:540px;width:1150px;height:470px;background:linear-gradient(#f7f7f7,var(--section-bg))}
.tile{top:567px;width:230px;height:144px;border:2px solid #fff;box-shadow:0 0 2px rgba(0,0,0,.25);overflow:hidden;color:#fff;font-weight:700}
.tile-ent{left:86px;background:var(--red)}
.tile-ent .label{position:absolute;left:30px;top:16px;width:166px;height:57px;background:#fff;color:var(--teal);font-size:16px;line-height:22px;padding:5px 8px}
.tile-ent .label span{display:block;text-align:right}
.tile-ent .visual{position:absolute;left:30px;top:56px;width:140px;height:88px;background:linear-gradient(#b70009,#7d1a1a)}
.tile-ai{left:335px;background:linear-gradient(110deg,#3f6f9a,#7aa0c0 55%,#dfe7ee)}
.tile-ai .label{position:absolute;left:10px;top:46px;font-size:16px;line-height:22px}
.tile-hotel{left:584px;background:var(--brown);text-align:center}
.tile-hotel .name{position:absolute;left:0;right:0;top:47px;font-size:18px;letter-spacing:.5px}
.tile-hotel .sub{position:absolute;left:0;right:0;top:71px;font-size:11px;font-weight:400;letter-spacing:1px}
.tile-hotel .cta{position:absolute;left:0;right:0;top:105px;font-size:16px}
.tile-health{left:833px;background:radial-gradient(circle at 25% 60%,#c23a2e 0%,#3b5aa8 35%,#1f52a8 70%,#0e3f8a)}
.tile-health .label{position:absolute;right:12px;top:13px;font-size:16px}
.plan{top:738px;width:230px;height:243px;color:#fff}
.plan-join{left:86px;background:var(--teal-tile)}
.plan-join .arrow{position:absolute;left:230px;top:17px}
.plan-join p{position:absolute;left:0;right:0;top:148px;text-align:center;font-weight:700;font-size:16.5px;line-height:22px}
.plan-ent{left:335px;background:var(--plan-ent)}
.plan-pro{left:584px;background:var(--plan-pro)}
.plan-per{left:833px;background:var(--plan-per)}
.plan h2{font-size:16.5px;text-align:center;margin-top:10px;font-weight:700}
.plan ul{list-style:none;margin:17px 0 0 17px;width:205px}
.plan li{position:relative;padding-left:24px;font-size:13.4px;line-height:16px;margin-bottom:14px}
.plan li svg{position:absolute;left:0;top:1px}
.plan-btn{position:absolute;left:17px;top:182px;width:201px;height:45px;background:linear-gradient(#fff,#ececec);border-radius:2px;color:#333;font-weight:700;font-size:16px;display:flex;align-items:center;justify-content:center;gap:12px}
.footer{left:0;top:1010px;width:1150px;height:90px;background:var(--footer-bg);color:var(--footer-text);font-size:12px}
.footer-links{position:absolute;left:85px;top:22px}
.footer-links span{margin:0 8px;color:#888}
.footer-copy{position:absolute;left:85px;top:54px;word-spacing:2px}
.social{position:absolute;top:29px;width:32px;height:32px;background:linear-gradient(#fafafa,#ddd);border-radius:3px}
.tag{position:absolute;right:8px;bottom:8px;font-size:13px;color:#bbb}
</style>
</head>
<body>
<div class="page">
  <div class="abs topline"></div>
  <header class="abs header"></header>
  <div class="abs brand"><span class="brand-name">my LUMENFOLD</span><span class="brand-mark"></span></div>
  <div class="abs account"><span class="btn-dark">REGISTER</span><span class="btn-dark">LOG IN</span></div>

  <section class="abs hero"></section>
  <nav class="abs nav">
    <a class="active" style="width:92px">HOME</a>
    <a style="width:145px">TECHNOLOGY</a>
    <a style="width:122px">PRODUCTS</a>
    <a style="width:170px">OUR LUMENFOLDS</a>
    <a style="width:91px">NEWS</a>
    <a style="width:111px">COMPANY</a>
    <div class="search">Search
      <svg width="16" height="16" viewBox="0 0 16 16"><circle cx="6" cy="6" r="4.5" fill="none" stroke="#222" stroke-width="2.2"/><line x1="9.5" y1="9.5" x2="14.5" y2="14.5" stroke="#222" stroke-width="3" stroke-linecap="round"/></svg>
    </div>
  </nav>

  <h1 class="abs hero-title">Welcome to My Lumenfold</h1>
  <p class="abs hero-copy">Donec et tristique magna, vel accumsan lectus. Duis vitae mi odio. Mauris vitae fringilla quam. Quisque iaculis semper mauris, nec vestibu lum turpis. Proin interdum imperdiet tincidunt. Cras eu diam lectus. Ut quis vehicula leo. Donec blandit quam nec eros vehicula, nec egestas nulla placerat. Sed ut convallis nisl, ac tincidunt nisl. Duis sollicitudin arcu metus, ut volutpat sem molestie ac.</p>
  <span class="abs btn-dark hero-more">VIEW MORE</span>
  <div class="abs dots"><span class="on"></span><span></span><span></span><span></span></div>

  <div class="abs monitor">
    <div class="screen" role="img" aria-label="Video still of a banking website with a virtual assistant panel"></div>
    <div class="play"><svg width="72" height="50" viewBox="0 0 72 50"><polygon points="28,13 28,37 48,25" fill="#fff"/></svg></div>
    <div class="chin"></div>
  </div>
  <svg class="abs stand" width="128" height="52" viewBox="0 0 128 52"><path d="M18 0 H110 L122 44 Q124 50 116 50 H12 Q4 50 6 44 Z" fill="#c4c4c4"/><path d="M18 0 H110 L112 8 H16 Z" fill="#8e8e8e"/></svg>

  <div class="abs sep"></div>
  <section class="abs section"></section>

  <div class="abs tile tile-ent">
    <div class="visual" role="img" aria-label="Virtual assistant avatar with video play button"></div>
    <div class="label">Our Enterprise<span>Customers</span></div>
  </div>
  <div class="abs tile tile-ai" role="img" aria-label="Hand touching a network of technology icons">
    <div class="label">Artificial<br>Intelligence<br>for Customer<br>Suopport</div>
  </div>
  <div class="abs tile tile-hotel">
    <div class="name">Karuna Selatan</div>
    <div class="sub">HOTELS &amp; RESORTS</div>
    <div class="cta">Small Business Solutions</div>
  </div>
  <div class="abs tile tile-health" role="img" aria-label="Glowing heart with heartbeat line">
    <div class="label">Health Coach</div>
  </div>

  <div class="abs plan plan-join">
    <svg class="arrow" width="18" height="32" viewBox="0 0 18 32"><polygon points="0,0 18,16 0,32" fill="#4aae99"/></svg>
    <p>Sign up today and make<br>your own Lumenfold<br>for free</p>
  </div>

  <div class="abs plan plan-ent">
    <h2>Enterprise</h2>
    <ul>
      <li><svg width="13" height="13" viewBox="0 0 13 13"><circle cx="6.5" cy="6.5" r="5.2" fill="none" stroke="#fff" stroke-width="1.6"/><path d="M3.6 6.6 L6 9 L12.5 2" fill="none" stroke="#fff" stroke-width="2"/></svg>Advanced customer support</li>
      <li><svg width="13" height="13" viewBox="0 0 13 13"><circle cx="6.5" cy="6.5" r="5.2" fill="none" stroke="#fff" stroke-width="1.6"/><path d="M3.6 6.6 L6 9 L12.5 2" fill="none" stroke="#fff" stroke-width="2"/></svg>Sophisticated visual avatar</li>
      <li><svg width="13" height="13" viewBox="0 0 13 13"><circle cx="6.5" cy="6.5" r="5.2" fill="none" stroke="#fff" stroke-width="1.6"/><path d="M3.6 6.6 L6 9 L12.5 2" fill="none" stroke="#fff" stroke-width="2"/></svg>Advanced analytics</li>
      <li><svg width="13" height="13" viewBox="0 0 13 13"><circle cx="6.5" cy="6.5" r="5.2" fill="none" stroke="#fff" stroke-width="1.6"/><path d="M3.6 6.6 L6 9 L12.5 2" fill="none" stroke="#fff" stroke-width="2"/></svg>Speech to Text capabilities</li>
    </ul>
    <div class="plan-btn"><svg width="18" height="18" viewBox="0 0 18 18"><circle cx="9" cy="9" r="9" fill="#444"/><path d="M7.5 5 L11.5 9 L7.5 13" fill="none" stroke="#fff" stroke-width="2"/></svg>Enquire Now</div>
  </div>

  <div class="abs plan plan-pro">
    <h2>Professional</h2>
    <ul>
      <li><svg width="13" height="13" viewBox="0 0 13 13"><circle cx="6.5" cy="6.5" r="5.2" fill="none" stroke="#fff" stroke-width="1.6"/><path d="M3.6 6.6 L6 9 L12.5 2" fill="none" stroke="#fff" stroke-width="2"/></svg>&nbsp;Sign up for Beta access</li>
      <li><svg width="13" height="13" viewBox="0 0 13 13"><circle cx="6.5" cy="6.5" r="5.2" fill="none" stroke="#fff" stroke-width="1.6"/><path d="M3.6 6.6 L6 9 L12.5 2" fill="none" stroke="#fff" stroke-width="2"/></svg>Quick and easy to set up</li>
      <li><svg width="13" height="13" viewBox="0 0 13 13"><circle cx="6.5" cy="6.5" r="5.2" fill="none" stroke="#fff" stroke-width="1.6"/><path d="M3.6 6.6 L6 9 L12.5 2" fill="none" stroke="#fff" stroke-width="2"/></svg>Low cost – Ideal for small business</li>
    </ul>
    <div class="plan-btn"><svg width="18" height="18" viewBox="0 0 18 18"><circle cx="9" cy="9" r="9" fill="#444"/><path d="M7.5 5 L11.5 9 L7.5 13" fill="none" stroke="#fff" stroke-width="2"/></svg>Free Trial</div>
  </div>

  <div class="abs plan plan-per">
    <h2>Personal</h2>
    <ul>
      <li><svg width="13" height="13" viewBox="0 0 13 13"><circle cx="6.5" cy="6.5" r="5.2" fill="none" stroke="#fff" stroke-width="1.6"/><path d="M3.6 6.6 L6 9 L12.5 2" fill="none" stroke="#fff" stroke-width="2"/></svg>Instant results</li>
      <li><svg width="13" height="13" viewBox="0 0 13 13"><circle cx="6.5" cy="6.5" r="5.2" fill="none" stroke="#fff" stroke-width="1.6"/><path d="M3.6 6.6 L6 9 L12.5 2" fill="none" stroke="#fff" stroke-width="2"/></svg>Super easy to set up</li>
      <li><svg width="13" height="13" viewBox="0 0 13 13"><circle cx="6.5" cy="6.5" r="5.2" fill="none" stroke="#fff" stroke-width="1.6"/><path d="M3.6 6.6 L6 9 L12.5 2" fill="none" stroke="#fff" stroke-width="2"/></svg>Instant access</li>
      <li><svg width="13" height="13" viewBox="0 0 13 13"><circle cx="6.5" cy="6.5" r="5.2" fill="none" stroke="#fff" stroke-width="1.6"/><path d="M3.6 6.6 L6 9 L12.5 2" fill="none" stroke="#fff" stroke-width="2"/></svg>Not suitable for commercial use</li>
    </ul>
    <div class="plan-btn"><svg width="18" height="18" viewBox="0 0 18 18"><circle cx="9" cy="9" r="9" fill="#444"/><path d="M7.5 5 L11.5 9 L7.5 13" fill="none" stroke="#fff" stroke-width="2"/></svg>Free Registration</div>
  </div>

  <footer class="abs footer">
    <div class="footer-links">Home<span>|</span>Technology<span>|</span>Products<span>|</span>Our Lumenfolds<span>|</span>News<span>|</span>Company</div>
    <div class="footer-copy">Copyright &nbsp;©&nbsp;&nbsp; 2013 &nbsp;&nbsp;www.mylumenfold.example &nbsp;&nbsp;&nbsp;All rights reserved.</div>
    <span class="social" style="left:985px"></span>
    <span class="social" style="left:1033px"></span>
    <span class="tag">M2</span>
  </footer>
</div>
</body>
</html>
```